Business acrd and Stationery desgin FOR DUNMORE

I want creative and expressive stationary design .on the front side for business card I need the logo and doctors name to be there and on the back side I need time and appointment .Please see attached business card to use same names ,but use address below and phone number

Note:the deigner must submit the file in vector format and PSD and PDF

Business name is :Dunmore Glen Medical Clinic.

Address:
20418 57 ST NW
City :EDMONTON AB
Postal code: T6K 3R8

Phone :(780) 555-0142
Fax:(780) 555-0187

Other Business name :Dunmore Medical Clinic

• logo in the back on business card

```html
<!DOCTYPE html>
<html lang="en">
<head>
<meta charset="utf-8">
<title>Dunmore Glen Medical Clinic – Stationery</title>
<link rel="stylesheet" href="https://fonts.googleapis.com/css2?family=Cinzel:wght@600&family=Questrial&family=Pinyon+Script&display=swap">
<style>
  :root {
    --navy: #2c3a8c;
    --red: #d8232a;
    --paper: #ffffff;
    --ground: #d9d9db;
    --ink: #3a3a3a;
    --muted: #6b6b6b;
    --rule: #b9b9c4;
  }
  * { box-sizing: border-box; margin: 0; padding: 0; }
  html, body { width: 1200px; height: 1118px; overflow: hidden; }
  body {
    background: var(--ground);
    font-family: "Questrial", "Century Gothic", sans-serif;
    color: var(--ink);
    position: relative;
  }
  .sheet { position: absolute; background: var(--paper); overflow: hidden; }
  .sheet--bands { border-top: 5px solid var(--red); border-bottom: 7px solid var(--navy); }

  /* brand block */
  .brand { display: flex; align-items: center; gap: 6px; }
  .brand__dot { width: 12px; height: 12px; border-radius: 50%; background: var(--red); flex: none; }
  .brand__name {
    font-family: "Cinzel", "Times New Roman", serif;
    font-weight: 600; color: var(--navy);
    font-size: 10px; line-height: 1.1; letter-spacing: .02em;
    white-space: nowrap;
  }
  .brand--light .brand__name { color: #fff; }

  /* letterhead */
  .letterhead { left: 188px; top: 60px; width: 382px; height: 540px; }
  .letterhead .brand { position: absolute; left: 38px; top: 36px; }
  .contact { position: absolute; font-size: 5.5px; line-height: 1.6; color: var(--ink); white-space: nowrap; }
  .contact--head { right: 34px; top: 38px; display: flex; gap: 10px; }
  .contact__phones span { display: flex; align-items: center; gap: 3px; }
  .icon { width: 6px; height: 6px; flex: none; }
  .letter { position: absolute; left: 38px; right: 38px; top: 102px; font-size: 5.6px; line-height: 1.55; }
  .letter__date, .letter__to { margin-bottom: 18px; }
  .letter__greeting { font-weight: bold; margin: 10px 0 8px; }
  .letter p { margin-bottom: 8px; }
  .letter__sign { display: flex; align-items: flex-end; gap: 8px; margin-top: 10px; }
  .letter__name { font-weight: bold; }
  .signature { width: 58px; height: 28px; background: linear-gradient(90deg, #dfe3f4, #c8cfee); border-radius: 3px; }

  /* folder */
  .folder { left: 616px; top: 47px; width: 416px; height: 553px; background: var(--navy); border-bottom: 6px solid var(--red); }
  .folder__spine { position: absolute; top: 0; bottom: 0; left: 22px; width: 6px; border-left: 1px solid rgba(255,255,255,.15); border-right: 1px solid rgba(0,0,0,.15); }
  .folder .brand { position: absolute; left: 142px; top: 84px; }
  .folder .brand__name { font-size: 13px; }
  .folder .brand__dot { width: 15px; height: 15px; }

  /* envelope front */
  .envelope { left: 170px; top: 646px; width: 400px; height: 200px; }
  .envelope .brand { position: absolute; left: 22px; top: 26px; }
  .envelope__address { position: absolute; left: 36px; bottom: 10px; font-size: 5.5px; }

  /* envelope back */
  .envelope-back { left: 616px; top: 646px; width: 399px; height: 200px; border: 1px solid #e6e6e6; }
  .envelope-back svg { position: absolute; left: 0; top: 0; }
  .envelope-back__name { position: absolute; left: 0; right: 0; top: 22px; text-align: center; font-family: "Cinzel", serif; font-weight: 600; color: #fff; font-size: 8px; }

  /* business cards */
  .card { top: 891px; width: 162px; height: 93px; border: 1px solid #e4e4e4; }
  .card--front { left: 196px; border-bottom: 5px solid var(--navy); }
  .card__doctors { position: absolute; left: 10px; top: 20px; font-size: 4.8px; font-weight: bold; line-height: 1.5; color: var(--navy); white-space: nowrap; }
  .card--front .brand { position: absolute; left: 72px; top: 17px; gap: 3px; }
  .card .brand__name { font-size: 5.4px; }
  .card .brand__dot { width: 6px; height: 6px; }
  .card__tagline { position: absolute; left: 10px; top: 62px; font-size: 4.2px; line-height: 1.5; color: var(--red); white-space: nowrap; }
  .card__contact { position: absolute; left: 70px; top: 66px; display: flex; gap: 8px; font-size: 3.8px; line-height: 1.6; white-space: nowrap; }
  .card__contact-phones div { display: flex; align-items: center; gap: 2px; }
  .card__contact .icon { width: 4px; height: 4px; }

  .card--back { left: 406px; border-bottom: 5px solid var(--navy); }
  .card__band { height: 28px; background: var(--navy); position: relative; }
  .card__band .brand { position: absolute; left: 8px; top: 8px; gap: 3px; }
  .card__band-label { position: absolute; right: 8px; top: 12px; font-size: 3.8px; color: #fff; font-weight: bold; white-space: nowrap; }
  .appointments { list-style: none; padding: 10px 12px 0 12px; font-size: 4px; color: var(--muted); }
  .appointments li { display: flex; align-items: flex-end; gap: 3px; height: 11px; }
  .appointments .blank { flex: 1; border-bottom: .6px solid var(--rule); }
  .appointments .blank--short { flex: 0 0 16px; }

  /* compliments slip */
  .slip { left: 616px; top: 892px; width: 382px; height: 181px; }
  .slip .brand { position: absolute; left: 24px; top: 24px; }
  .contact--slip { left: 44px; bottom: 12px; display: flex; gap: 10px; }
  .slip__compliments { position: absolute; right: 30px; bottom: 12px; font-family: "Pinyon Script", cursive; font-size: 19px; color: var(--navy); }
  .slip__compliments em { font-style: normal; color: var(--red); }
</style>
</head>
<body>

<svg width="0" height="0" style="position:absolute" aria-hidden="true">
  <symbol id="phone" viewBox="0 0 10 10"><rect width="10" height="10" rx="1.5" fill="#d8232a"/><path d="M3 2.2l1.2 1.6-.7.8c.4.9 1 1.5 1.9 1.9l.8-.7 1.6 1.2-.7 1.1C4.6 7.8 2.2 5.4 2 3z" fill="#fff"/></symbol>
  <symbol id="fax" viewBox="0 0 10 10"><rect width="10" height="10" rx="1.5" fill="#d8232a"/><rect x="2.5" y="4" width="5" height="3.5" fill="#fff"/><rect x="3.5" y="2" width="3" height="2" fill="#fff"/></symbol>
</svg>

<!-- Letterhead -->
<section class="sheet sheet--bands letterhead">
  <div class="brand"><span class="brand__dot"></span><span class="brand__name">Dunmore Glen<br>Medical Clinic</span></div>
  <div class="contact contact--head">
    <div>20418 57 ST NW<br>Edmonton AB, T6K 3R8</div>
    <div class="contact__phones">
      <span><svg class="icon"><use href="#phone"/></svg>(780) 555-0142</span>
      <span><svg class="icon"><use href="#fax"/></svg>(780) 555-0187</span>
    </div>
  </div>
  <article class="letter">
    <div class="letter__date">30.02.2015</div>
    <div class="letter__to">Recipient's name<br>Lindenweg 8<br>20144 Hamburg<br>Germany</div>
    <div class="letter__greeting">Dear sir,</div>
    <p>Clear communication sits at the heart of good care. Whether we speak in person, by telephone or in writing, every message we send should help patients understand their health and feel confident about the next step in their treatment.</p>
    <p>Letters remain an important part of that work. Referrals, results and reminders are often kept for years, so we take care that each one is accurate, easy to read and sent on time to the right person.</p>
    <p>Our team reviews every letter before it leaves the clinic. If anything is unclear, please call us and a member of staff will be glad to explain the details or arrange a follow-up visit at a time that suits you.</p>
    <p>Thank you for your continued trust in our clinic. We look forward to seeing you again soon.</p>
    <div class="letter__sign">
      <div>Yours Sincerely,<br><span class="letter__name">Lena Marsh</span></div>
      <div class="signature" role="img" aria-label="Handwritten signature"></div>
    </div>
  </article>
</section>

<!-- Presentation folder -->
<section class="sheet folder">
  <div class="folder__spine"></div>
  <div class="brand brand--light"><span class="brand__dot"></span><span class="brand__name">Dunmore Glen<br>Medical Clinic</span></div>
</section>

<!-- Envelope front -->
<section class="sheet sheet--bands envelope">
  <div class="brand"><span class="brand__dot"></span><span class="brand__name">Dunmore Glen<br>Medical Clinic</span></div>
  <div class="envelope__address">20418 57 ST NW, Edmonton AB, PO: T6K 3R8</div>
</section>

<!-- Envelope back -->
<section class="sheet envelope-back">
  <svg width="399" height="58" viewBox="0 0 399 58"><path d="M0 0H399V10L384 58H15L0 10Z" fill="#2c3a8c"/></svg>
  <div class="envelope-back__name">Dunmore Glen Medical Clinic</div>
</section>

<!-- Business card front -->
<section class="sheet card card--front">
  <div class="card__doctors">Dr A KESTRAVI<br>Dr Z HOLLOWAY</div>
  <div class="brand"><span class="brand__dot"></span><span class="brand__name">Dunmore Glen<br>Medical Clinic</span></div>
  <div class="card__tagline">Family Doctors<br>Family Practice<br>&amp; walk in welcome</div>
  <div class="card__contact">
    <div>20418 57 ST NW<br>Edmonton AB, T6K 3R8</div>
    <div class="card__contact-phones">
      <div><svg class="icon"><use href="#phone"/></svg>(780) 555-0142</div>
      <div><svg class="icon"><use href="#fax"/></svg>(780) 555-0187</div>
    </div>
  </div>
</section>

<!-- Business card back -->
<section class="sheet card card--back">
  <div class="card__band">
    <div class="brand brand--light"><span class="brand__dot"></span><span class="brand__name">Dunmore<br>Medical Clinic</span></div>
    <div class="card__band-label">YOUR APPOINTMENT</div>
  </div>
  <ol class="appointments">
    <li>1.<span class="blank blank--short"></span>am/pm<span class="blank"></span>__/__/__</li>
    <li>2.<span class="blank blank--short"></span>am/pm<span class="blank"></span>__/__/__</li>
    <li>3.<span class="blank blank--short"></span>am/pm<span class="blank"></span>__/__/__</li>
    <li>4.<span class="blank blank--short"></span>am/pm<span class="blank"></span>__/__/__</li>
  </ol>
</section>

<!-- Compliments slip -->
<section class="sheet sheet--bands slip">
  <div class="brand"><span class="brand__dot"></span><span class="brand__name">Dunmore Glen<br>Medical Clinic</span></div>
  <div class="contact contact--slip">
    <div>20418 57 ST NW<br>Edmonton AB, T6K 3R8</div>
    <div class="contact__phones">
      <span><svg class="icon"><use href="#phone"/></svg>(780) 555-0142</span>
      <span><svg class="icon"><use href="#fax"/></svg>(780) 555-0187</span>
    </div>
  </div>
  <div class="slip__compliments"><em>With</em> Compliments</div>
</section>

</body>
</html>
```